The Plate Compass

Cutting Through the Noise to What Actually Works.

Nutrition book

Target Market(s)

People looking to be or get healthy and eat right.

```html
<!DOCTYPE html>
<html lang="en">
<head>
<meta charset="utf-8">
<title>The Plate Compass — Book Cover</title>
<link rel="stylesheet" href="https://fonts.googleapis.com/css2?family=DM+Serif+Display&family=Montserrat:wght@500;600&family=Oswald:wght@600&display=swap">
<style>
  :root {
    --backdrop: #efece6;
    --paper: #ffffff;
    --forest: #143d2a;
    --lime: #7ccf1e;
    --lime-badge: #c6ec2a;
    --collage-light: #d9d9d9;
    --collage-dark: #9a9a9a;
    --collage-ink: #5d5d5d;
    --food-green: #5f8f3a;
    --food-cream: #e9e2b8;
  }
  * { margin: 0; padding: 0; box-sizing: border-box; }
  html, body {
    width: 1200px; height: 1200px; overflow: hidden;
    background: var(--backdrop);
  }
  .book-cover {
    position: absolute; left: 220px; top: 40px;
    width: 760px; height: 1120px;
    background: var(--paper);
    box-shadow: 0 12px 40px rgba(0,0,0,0.18);
    overflow: hidden;
  }
  .collage-side { position: absolute; inset: 0; }
  .collage-word {
    font-family: 'Oswald', sans-serif;
    font-weight: 600;
    fill: var(--collage-ink);
    letter-spacing: 1px;
  }
  .title-block {
    position: absolute; right: 30px; top: 190px;
    font-family: 'DM Serif Display', serif;
    font-weight: 400;
    line-height: 0.92;
    text-align: right;
  }
  .title-lead { color: var(--lime); font-size: 52px; display: block; text-align: left; padding-left: 130px; }
  .title-main { color: var(--forest); font-size: 104px; display: block; }
  .title-accent { color: var(--lime); font-size: 104px; display: block; }
  .title-swoosh { position: absolute; left: 430px; top: 450px; }
  .subtitle {
    position: absolute; left: 300px; top: 490px; width: 430px;
    font-family: 'DM Serif Display', serif;
    font-size: 33px; line-height: 1.15;
    color: var(--forest);
    text-align: center;
  }
  .promise-badge {
    position: absolute; left: 530px; top: 670px;
    width: 200px; height: 200px; border-radius: 50%;
    background: var(--lime-badge);
    display: flex; flex-direction: column; align-items: center; justify-content: center;
    font-family: 'Montserrat', sans-serif; font-weight: 500;
    font-size: 15px; letter-spacing: 3px; line-height: 1.45;
    color: var(--forest); text-align: center;
  }
  .promise-badge .badge-rule { width: 34px; height: 1px; background: var(--forest); margin-top: 6px; }
  .food-art {
    position: absolute; left: 215px; top: 650px;
    width: 330px; height: 350px;
    border-radius: 48% 52% 40% 45%;
    background: radial-gradient(circle at 55% 50%, var(--food-cream) 0%, #b9c76a 35%, var(--food-green) 70%, rgba(95,143,58,0) 72%);
  }
  .author-name {
    position: absolute; left: 300px; top: 1030px;
    font-family: 'Montserrat', sans-serif; font-weight: 500;
    font-size: 22px; letter-spacing: 8px;
    color: var(--forest);
  }
</style>
</head>
<body>
  <main class="book-cover">
    <svg class="collage-side" width="760" height="1120" viewBox="0 0 760 1120" role="img" aria-label="Torn grey newspaper collage of diet trend headlines">
      <defs>
        <linearGradient id="collageTone" x1="0" y1="0" x2="1" y2="1">
          <stop offset="0" stop-color="var(--collage-dark)"/>
          <stop offset="0.5" stop-color="var(--collage-light)"/>
          <stop offset="1" stop-color="var(--collage-dark)"/>
        </linearGradient>
      </defs>
      <path d="M0 0 L400 0 L385 40 L392 80 L370 120 L374 160 L350 190 L354 230 L330 260 L334 300 L310 330 L314 370 L292 400 L296 440 L276 470 L280 510 L262 540 L266 580 L248 610 L252 650 L236 680 L240 720 L224 750 L228 790 L212 830 L216 870 L204 900 L210 940 L200 975 L210 1010 L202 1050 L214 1085 L208 1120 L0 1120 Z" fill="url(#collageTone)" stroke="#f4f4f4" stroke-width="6"/>
      <g text-anchor="end">
        <text class="collage-word" x="360" y="62" font-size="46">KETO</text>
        <text class="collage-word" x="352" y="104" font-size="26">PLANT-BASED</text>
        <text class="collage-word" x="335" y="144" font-size="26">INTERMITTENT</text>
        <text class="collage-word" x="325" y="180" font-size="28">FASTING</text>
        <text class="collage-word" x="295" y="300" font-size="32">HIGH</text>
        <text class="collage-word" x="290" y="332" font-size="24">PROTEIN</text>
        <text class="collage-word" x="245" y="470" font-size="24">EAT FAT</text>
        <text class="collage-word" x="245" y="506" font-size="32">VEGAN</text>
      </g>
      <text class="collage-word" x="20" y="1040" font-size="40">TRENDY</text>
    </svg>

    <h1 class="title-block">
      <span class="title-lead">The</span>
      <span class="title-main">Plate</span>
      <span class="title-accent">Compass</span>
    </h1>
    <svg class="title-swoosh" width="300" height="30" viewBox="0 0 300 30">
      <path d="M5 12 Q150 2 295 22" stroke="var(--lime)" stroke-width="5" fill="none" stroke-linecap="round"/>
    </svg>

    <p class="subtitle">Cutting through the noise<br>to what actually works.</p>

    <div class="food-art" role="img" aria-label="Fresh whole foods: halved avocado, kale, blueberries, almonds, seeds and basil leaves"></div>

    <div class="promise-badge">
      <span>LESS</span>
      <span>CONFUSION</span>
      <span>BETTER</span>
      <span>CHOICES</span>
      <span>A HEALTHIER</span>
      <span>YOU</span>
      <span class="badge-rule"></span>
    </div>

    <p class="author-name">YOUR NAME HERE</p>
  </main>
</body>
</html>
```